Client Handbook for Modern building company

We are seeking a cover for our client handbook for print and eBook, would like it to be modern and streamlined, this will be a first impression when starting a project for a new client. possibly containing the photo of one of our projects (attached) or something resembling a successful relationship with a client? handshake etc

Requirements
Must have
• Our logo (attached) and our tagline "creating tomorrow" , the words Client Handbook,

```html
<!DOCTYPE html>
<html lang="en">
<head>
<meta charset="utf-8">
<title>Farbrook Builders – Client Handbook</title>
<link rel="stylesheet" href="https://fonts.googleapis.com/css2?family=Jost:wght@500&family=Oswald:wght@400&family=Source+Sans+3:wght@400&display=swap">
<style>
  :root {
    --navy-title: #0d3566;
    --ink: #111111;
    --night: #0d1020;
    --white: #ffffff;
    --frame-blue: #1c21a3;
    --frame-red: #e6304c;
    --sky-top: #f4f8fb;
    --sky-mid: #dce9f2;
    --leaf-light: #8cc83f;
    --leaf-deep: #3f7a22;
    --pavement: #c3c6ca;
  }
  * { margin: 0; padding: 0; box-sizing: border-box; }
  html, body { width: 855px; height: 1200px; overflow: hidden; background: var(--night); }
  .cover {
    position: relative;
    width: 855px;
    height: 1200px;
    overflow: hidden;
    background: var(--night);
    font-family: "Source Sans 3", sans-serif;
  }
  .backdrop-photo {
    position: absolute;
    left: 0; top: 0;
    width: 855px; height: 904px;
    background:
      radial-gradient(ellipse 190px 230px at 70px 520px, rgba(110,178,50,0.95) 0%, rgba(90,160,45,0.85) 45%, rgba(90,160,45,0) 100%),
      radial-gradient(ellipse 200px 240px at 800px 540px, rgba(120,186,55,0.95) 0%, rgba(95,165,45,0.85) 45%, rgba(95,165,45,0) 100%),
      radial-gradient(ellipse 130px 140px at 230px 600px, rgba(70,140,40,0.8) 0%, rgba(70,140,40,0) 100%),
      radial-gradient(ellipse 120px 130px at 660px 610px, rgba(70,140,40,0.8) 0%, rgba(70,140,40,0) 100%),
      radial-gradient(ellipse 70px 250px at 830px 260px, rgba(200,210,220,0.9) 0%, rgba(200,210,220,0) 100%),
      radial-gradient(ellipse 40px 90px at 265px 480px, rgba(80,160,220,0.7) 0%, rgba(80,160,220,0) 100%),
      radial-gradient(ellipse 40px 110px at 595px 470px, rgba(150,210,230,0.6) 0%, rgba(150,210,230,0) 100%),
      radial-gradient(ellipse 140px 60px at 60px 290px, rgba(255,255,255,0.9) 0%, rgba(255,255,255,0) 100%),
      linear-gradient(180deg,
        var(--sky-top) 0%,
        #e4eef5 20%,
        var(--sky-mid) 38%,
        #eaf0f3 55%,
        #d2dde0 70%,
        #bfc4c8 78%,
        var(--pavement) 100%);
  }
  .brand {
    position: absolute;
    top: 31px; left: 0; width: 855px; height: 52px;
    display: flex; justify-content: center; align-items: center; gap: 12px;
  }
  .brand-mark {
    width: 50px; height: 50px; border-radius: 50%;
    background: var(--ink);
  }
  .brand-name {
    font-family: "Jost", sans-serif;
    font-weight: 500;
    font-size: 26px;
    letter-spacing: 1px;
    color: var(--ink);
  }
  .tagline {
    position: absolute;
    left: 0; width: 855px;
    text-align: center;
    font-family: "Jost", sans-serif;
    font-weight: 500;
    color: var(--navy-title);
    line-height: 1;
    font-size: 116px;
    letter-spacing: -1px;
    transform-origin: center;
  }
  .tagline-top { top: 92px; transform: scaleX(0.8); }
  .tagline-bottom { top: 198px; transform: scaleX(0.84); }
  .doc-title {
    position: absolute;
    top: 309px; left: 0; width: 855px;
    text-align: center;
    font-family: "Oswald", sans-serif;
    font-weight: 400;
    font-size: 40px;
    letter-spacing: 2px;
    color: var(--ink);
    line-height: 1;
  }
  .hex-gallery { position: absolute; left: 0; top: 0; }
  .intro {
    position: absolute;
    top: 1010px; left: 0; width: 855px;
    text-align: center;
    color: var(--white);
  }
  .intro-heading { font-size: 28px; line-height: 1.2; margin-bottom: 5px; }
  .intro-text { font-size: 14.2px; line-height: 17px; }
  .contact-row {
    position: absolute;
    top: 1126px; left: 0; width: 855px; height: 30px;
  }
  .contact-item {
    position: absolute; top: 0;
    display: flex; align-items: center; gap: 13px;
    color: var(--white); font-size: 17px;
  }
  .contact-item svg { width: 30px; height: 30px; }
  .contact-phone { left: 125px; }
  .contact-mail { left: 346px; }
  .contact-web { left: 567px; }
</style>
</head>
<body>
<main class="cover">
  <div class="backdrop-photo" role="img" aria-label="Photo of a tree-lined plaza with glass office towers under a bright sky"></div>

  <header class="brand">
    <span class="brand-mark"></span>
    <span class="brand-name">FARBROOK BUILDERS</span>
  </header>

  <h1>
    <span class="tagline tagline-top">CREATING</span>
    <span class="tagline tagline-bottom">TOMORROW</span>
  </h1>
  <h2 class="doc-title">CLIENT HANDBOOK</h2>

  <svg class="hex-gallery" width="855" height="1200" viewBox="0 0 855 1200">
    <defs>
      <linearGradient id="frameGradient" gradientUnits="userSpaceOnUse" x1="0" y1="440" x2="0" y2="1020">
        <stop offset="0" stop-color="var(--frame-blue)"/>
        <stop offset="0.68" stop-color="var(--frame-blue)"/>
        <stop offset="0.84" stop-color="#8a2a84"/>
        <stop offset="1" stop-color="var(--frame-red)"/>
      </linearGradient>
      <linearGradient id="houseSky" gradientUnits="userSpaceOnUse" x1="0" y1="450" x2="0" y2="953">
        <stop offset="0" stop-color="#9cc8f2"/>
        <stop offset="0.25" stop-color="#bcd8f0"/>
        <stop offset="0.32" stop-color="#4c4f54"/>
        <stop offset="0.55" stop-color="#6b7076"/>
        <stop offset="0.72" stop-color="#a9acb0"/>
        <stop offset="0.8" stop-color="#dedfe0"/>
        <stop offset="1" stop-color="#ececec"/>
      </linearGradient>
      <radialGradient id="houseSide" gradientUnits="userSpaceOnUse" cx="480" cy="650" r="110">
        <stop offset="0" stop-color="#d8dadd" stop-opacity="0.85"/>
        <stop offset="1" stop-color="#d8dadd" stop-opacity="0"/>
      </radialGradient>
      <linearGradient id="deskTone" gradientUnits="userSpaceOnUse" x1="74" y1="683" x2="359" y2="1010">
        <stop offset="0" stop-color="#7a5638"/>
        <stop offset="0.45" stop-color="#4a3020"/>
        <stop offset="1" stop-color="#6e4c30"/>
      </linearGradient>
      <radialGradient id="paperGlow" gradientUnits="userSpaceOnUse" cx="130" cy="780" r="90">
        <stop offset="0" stop-color="#f1ede6" stop-opacity="0.8"/>
        <stop offset="1" stop-color="#f1ede6" stop-opacity="0"/>
      </radialGradient>
      <radialGradient id="laptopGlow" gradientUnits="userSpaceOnUse" cx="290" cy="760" r="70">
        <stop offset="0" stop-color="#d6d8dc" stop-opacity="0.75"/>
        <stop offset="1" stop-color="#d6d8dc" stop-opacity="0"/>
      </radialGradient>
      <linearGradient id="planTone" gradientUnits="userSpaceOnUse" x1="0" y1="686" x2="0" y2="1010">
        <stop offset="0" stop-color="#a9bccb"/>
        <stop offset="0.4" stop-color="#d9dde0"/>
        <stop offset="0.62" stop-color="#c9a98a"/>
        <stop offset="0.8" stop-color="#4a4a55"/>
        <stop offset="1" stop-color="#1e2230"/>
      </linearGradient>
      <radialGradient id="handGlow" gradientUnits="userSpaceOnUse" cx="580" cy="860" r="70">
        <stop offset="0" stop-color="#f0c8b4" stop-opacity="0.7"/>
        <stop offset="1" stop-color="#f0c8b4" stop-opacity="0"/>
      </radialGradient>
    </defs>

    <g class="hex-project">
      <polygon points="427,440 656,563 656,836 427,963 200,836 200,563" fill="url(#frameGradient)"/>
      <g role="img" aria-label="Photo of a completed modern two-storey house with garage">
        <polygon points="427,450 647,568 647,831 427,953 209,831 209,568" fill="url(#houseSky)"/>
        <polygon points="427,450 647,568 647,831 427,953 209,831 209,568" fill="url(#houseSide)"/>
      </g>
    </g>
    <g class="hex-agreement">
      <polygon points="217,673 368,760 368,933 217,1020 65,933 65,760" fill="url(#frameGradient)"/>
      <g role="img" aria-label="Photo of a handshake over a desk with a contract and laptop">
        <polygon points="217,683 359,765 359,928 217,1010 74,928 74,765" fill="url(#deskTone)"/>
        <polygon points="217,683 359,765 359,928 217,1010 74,928 74,765" fill="url(#paperGlow)"/>
        <polygon points="217,683 359,765 359,928 217,1010 74,928 74,765" fill="url(#laptopGlow)"/>
      </g>
    </g>
    <g class="hex-planning">
      <polygon points="638,676 790,760 790,933 638,1020 486,933 486,760" fill="url(#frameGradient)"/>
      <g role="img" aria-label="Photo of a hand touching a screen of sketched business plans">
        <polygon points="638,686 781,765 781,928 638,1010 495,928 495,765" fill="url(#planTone)"/>
        <polygon points="638,686 781,765 781,928 638,1010 495,928 495,765" fill="url(#handGlow)"/>
      </g>
    </g>
  </svg>

  <section class="intro">
    <p class="intro-heading">Lorem ipsum</p>
    <p class="intro-text">Lorem ipsum dolor sit amet, consectetuer adipiscing elit, sed diam nonummy nibh euismod tincidunt<br>ut laoreet dolore magna aliquam erat volutpat.</p>
  </section>

  <footer class="contact-row">
    <div class="contact-item contact-phone">
      <svg viewBox="0 0 30 30" aria-hidden="true">
        <circle cx="15" cy="15" r="14" fill="none" stroke="#fff" stroke-width="1.5"/>
        <path d="M10.5 8.5c1-.8 2-.6 2.5.3l1.2 2.2c.4.8.2 1.5-.5 2l-.9.6c.7 1.7 2 3 3.6 3.7l.6-.9c.5-.7 1.2-.9 2-.5l2.2 1.2c.9.5 1.1 1.5.3 2.5-1.2 1.5-3 1.7-5 .7-3.2-1.6-5.6-4-7-7.2-.8-1.900-.6-3.500 1-4.6z" fill="#fff"/>
      </svg>
      <span>123 4567 8910</span>
    </div>
    <div class="contact-item contact-mail">
      <svg viewBox="0 0 30 30" aria-hidden="true">
        <circle cx="15" cy="15" r="14" fill="none" stroke="#fff" stroke-width="1.5"/>
        <rect x="8" y="10" width="14" height="10" fill="#fff"/>
        <path d="M8 10l7 5.5 7-5.5" fill="none" stroke="var(--night)" stroke-width="1.4"/>
      </svg>
      <span>mail@mail.com</span>
    </div>
    <div class="contact-item contact-web">
      <svg viewBox="0 0 30 30" aria-hidden="true">
        <g fill="none" stroke="#fff" stroke-width="1.6">
          <circle cx="15" cy="15" r="12"/>
          <ellipse cx="15" cy="15" rx="5" ry="12"/>
          <line x1="3" y1="15" x2="27" y2="15"/>
          <path d="M5 9h20M5 21h20"/>
          <line x1="15" y1="3" x2="15" y2="27"/>
        </g>
      </svg>
      <span>www.web.com</span>
    </div>
  </footer>
</main>
</body>
</html>
```